Brixelo Photography Business Cards

We need a good general business card that we can hand to our clients. We will be doing embossed gloss cards.

Target Market(s)

Real estate / Business to business / professionals

```html
<!DOCTYPE html>
<html lang="en">
<head>
<meta charset="utf-8">
<title>Brixelo Photography – Business Card</title>
<link rel="stylesheet" href="https://fonts.googleapis.com/css2?family=Arimo:wght@400;700&display=swap">
<style>
  :root {
    --backdrop: #2a2a2a;
    --card: #efefef;
    --ink: #8c8c8c;
    --ink-strong: #7a7a7a;
    --rule: #9a9a9a;
  }
  * { margin: 0; padding: 0; box-sizing: border-box; }
  html, body {
    width: 1093px;
    height: 1200px;
    overflow: hidden;
    background: var(--backdrop);
  }
  .canvas {
    position: relative;
    width: 1093px;
    height: 1200px;
    font-family: "Arimo", Arial, sans-serif;
  }
  .card {
    position: absolute;
    left: 264px;
    width: 580px;
    height: 357px;
    background: var(--card);
  }
  .card--front { top: 226px; }
  .card--back { top: 620px; }

  .contact {
    position: absolute;
    top: 66px;
    left: 0;
    width: 100%;
    text-align: center;
    color: var(--ink);
    font-size: 16px;
    line-height: 21px;
  }
  .contact__name {
    color: var(--ink-strong);
    font-weight: 700;
    font-size: 18px;
    line-height: 22px;
    letter-spacing: 0.2px;
  }
  .contact__rule {
    width: 143px;
    height: 1px;
    background: var(--rule);
    margin: 12px auto 14px;
  }
  .contact__label { font-weight: 700; }

  .brand {
    position: absolute;
    top: 0;
    left: 0;
    width: 100%;
    height: 100%;
    display: flex;
    align-items: center;
    justify-content: center;
  }
  .brand__name {
    color: var(--ink-strong);
    font-weight: 700;
    font-size: 30px;
    letter-spacing: 0.5px;
  }
</style>
</head>
<body>
<main class="canvas">
  <section class="card card--front">
    <div class="contact">
      <p class="contact__name">MARCUS DELANEY</p>
      <p class="contact__role">Managing Director</p>
      <div class="contact__rule"></div>
      <p><span class="contact__label">P:</span> 051-482 730 916</p>
      <p><span class="contact__label">M:</span> 051-482 730 917</p>
      <p><span class="contact__label">E:</span> hello@brixelo.com</p>
      <p><span class="contact__label">W:</span> www.brixelophoto.com</p>
      <div class="contact__rule"></div>
      <p>48 Larkfield Road, Suite 7</p>
      <p>Eastmoor, 204718</p>
    </div>
  </section>
  <section class="card card--back">
    <div class="brand">
      <p class="brand__name">Brixelo Photography</p>
    </div>
  </section>
</main>
</body>
</html>
```